5x8" package design for beauty / skin care product in a mylar bag

Brevona Works’ Glycolic Acid Powder is pure glycolic acid powder that, when mixed with water, creates glycolic acid solution. Depending on the amount of water added to the powder, you can create different strengths of the solution. Commerical products use between 10 and 70% glycolic acid solution in products. Brevona Works is part of the Calmora hair care company. One of our products use glycolic acid and we can repurpose the raw ingredient alone for retail sales targeting do-it-yourself at home beauty and skin care makers.

Most sellers of glycolic acid powder use basic packaging. Brevona Works intends to create professional, standout packaging that reinforces the quality of the glycolic acid powder we are selling and is consistent with other Calmora brand products sold.

Package design is for a 5x8" matte finished, top loading, resealable pouch. Just looking for front design initially. Second project will include back pouch design using format or design from the front of package.

```html
<!DOCTYPE html>
<html lang="en">
<head>
<meta charset="utf-8">
<title>Brevona Works Glycolic Acid Powder – Pouch Front</title>
<link rel="stylesheet" href="https://fonts.googleapis.com/css2?family=Montserrat:wght@300;400;500;700&display=swap">
<style>
  :root {
    --backdrop: #979797;
    --pattern-tone: #8fb3a7;
    --band-dark: #0f3f39;
    --panel-light-top: #a9c6bc;
    --panel-light-bottom: #7fa59a;
    --panel-dark-top: #2e5e56;
    --panel-dark-bottom: #133f38;
    --brand-green: #1f5a50;
    --chip: #8fb3a7;
    --ink-light: #f2f5f3;
    --placeholder-light: #b9cbc5;
    --placeholder-edge: #2a5a52;
  }
  * { margin: 0; padding: 0; box-sizing: border-box; }
  html, body { width: 1200px; height: 800px; overflow: hidden; }
  body {
    background: var(--backdrop);
    font-family: "Montserrat", sans-serif;
    position: relative;
  }
  .pouch {
    position: absolute;
    left: 392px;
    top: 80px;
    width: 410px;
    height: 634px;
    border-radius: 14px 14px 22px 22px;
    overflow: hidden;
    background: linear-gradient(180deg, var(--panel-dark-top), var(--panel-dark-bottom));
  }
  .pattern-strip {
    position: absolute; left: 0; top: 0; width: 100%; height: 37px;
    background: var(--pattern-tone);
  }
  .reseal-band {
    position: absolute; left: 0; top: 37px; width: 100%; height: 25px;
    background: var(--band-dark);
    color: var(--ink-light);
    font-size: 12px; font-weight: 500; letter-spacing: 3px;
    display: flex; align-items: center; justify-content: center;
  }
  .brand-panel {
    position: absolute; left: 0; top: 62px; width: 100%; height: 193px;
    background: linear-gradient(180deg, var(--panel-light-top), var(--panel-light-bottom));
  }
  .brand-name {
    position: absolute; left: 0; width: 100%; top: 70px;
    text-align: center;
    font-size: 40px; font-weight: 500; color: var(--brand-green);
    letter-spacing: 1px;
  }
  .product-band {
    position: absolute; left: 0; top: 255px; width: 100%; height: 95px;
    background: var(--band-dark);
    border-top: 2px solid #6f968b;
    border-bottom: 2px solid #6f968b;
    text-align: center;
  }
  .product-title {
    margin-top: 20px;
    font-size: 21px; font-weight: 500; letter-spacing: 1px;
    color: var(--ink-light);
  }
  .formula {
    display: inline-block; margin-top: 10px;
    background: var(--chip); color: var(--band-dark);
    font-size: 20px; font-weight: 300; letter-spacing: 2px;
    padding: 2px 16px 4px;
  }
  .formula sub { font-size: 12px; }
  .claim {
    position: absolute; right: 40px; top: 375px;
    text-align: center; color: var(--ink-light);
  }
  .claim-figure { font-size: 40px; font-weight: 700; line-height: 1; }
  .claim-note { font-size: 9.5px; font-weight: 500; letter-spacing: 1px; line-height: 1.3; margin-top: 4px; }
  .powder-visual {
    position: absolute; left: 55px; top: 440px; width: 292px; height: 112px;
    background: radial-gradient(ellipse at 50% 60%, var(--placeholder-light) 0%, var(--placeholder-edge) 100%);
  }
  .uses {
    position: absolute; left: 0; width: 100%; top: 564px;
    text-align: center; color: var(--ink-light);
    font-size: 9.5px; font-weight: 500; letter-spacing: 0.5px;
  }
  .net-weight {
    position: absolute; left: 0; width: 100%; top: 606px;
    text-align: center; color: var(--ink-light);
    font-size: 9px; font-weight: 500;
  }
</style>
</head>
<body>
  <main class="pouch">
    <div class="pattern-strip" role="img" aria-label="Soft sage decorative lattice pattern"></div>
    <div class="reseal-band">RESEALABLE BAG</div>
    <section class="brand-panel">
      <div class="brand-name">Brevona Works</div>
    </section>
    <section class="product-band">
      <h1 class="product-title">GLYCOLIC ACID POWDER</h1>
      <div class="formula">C<sub>2</sub>H<sub>4</sub>O<sub>3</sub></div>
    </section>
    <div class="claim">
      <div class="claim-figure">0%</div>
      <div class="claim-note">FRAGRANCES,<br>ADDITIVES, DYES</div>
    </div>
    <div class="powder-visual" role="img" aria-label="Photo of a pile of white glycolic acid powder with falling grains"></div>
    <p class="uses">FACIAL / TONER / SCALP SCRUB / HYPERPIGMENTATION</p>
    <p class="net-weight">NET WT. 100G</p>
  </main>
</body>
</html>
```